Fenwick and Torrance Postcard Design

Greetings!
Lawyers hire me as an expert witness. They take a gamble on hiring me in hopes of winning their case.
This postcard will be printed in jumbo size through Quillmark. The design must meet these specifications:

Full Bleed Size (starting document size)
11.12" x 6.12"
282 x 155 mm
3335 x 1835 pixels
* Finished artwork should use the full bleed dimensions for best results.
Document Trim Size (final size after being cut)
11.00" x 6.00"
279 x 152 mm
3300 x 1800 pixels
* Please be sure to keep all text and photos within the safe cutting margin.
Resolution
300 DPI
Visit Quillmark for more details or to download a design template:
https://www.quillmark-example.com/product-presentation-info.aspx?productPresentationId=1590#
https://www.quillmark-example.com/vp/ns/propath/UploadResources.aspx?selectedTab=0?pfid=BDW&pf_id=BDW&xnav=product-page#FileFormats

1. The postcard will have a Blank Backside.
2. I like a black, white and red color theme with a serious legalistic font.
3. In regards to color theme, see https://www.cardorbit-example.com/designs/security-system-postcards/#security-system-postcards-4
4. 8 preferred background images in alphabetical order from favorite to least favorite, but all are great:
a. https://files.driftbox-example.com/f/s!QwErTy12ZxCvBn34MnBvCx56LkJhGf
5. Header Text:
a. (line 1) Dr. K.R. Torrance, Psy.D., NCEB
b. (lines 2 and 3) Psychological Evaluator, Board-Certified Forensic Psychologist and National Expert Witness
c. (Line 4 in bold and more prominent than text in lines 1-3) 4 Signs of a Proficient & Credible Psyc. Expert
6. View this checklist image for inspiration, https://lnk.tidepoint-example.com/images/8RqWm3 and use the following text within such a checklist image:
7. Board Certified by the Continental Council of Courtroom Behavioral Science (CCCB)?
Yes, I'm Board Certified. This mark of proficiency in forensic psychology is recognized by judicial decisions, statutes and regulations.
8. Fellow of the Cont. Fellowship of Legal Behavioral Study?
Yes, I'm a CFLB Fellow, along with some of the field's most prominent leaders comprising the academic arm of the CCCB.
9. A Recognized Leader Amongst Other Experts?
I’m the 2018 duly elected President of the Hudson Valley Behavioral Guild Section on Courtroom Assessment, and a Board Member of the Coalition of Practitioners for Youth Safeguarding.
10. Positioned in Roles of Trust and Neutrality by Judges?
Yes, I work as an in-house Harborview Juvenile Tribunal mental-health expert in proceedings regarding competency, imminent risk, sentencing, custody, child maltreatment and TPR.
11. The following should be prominent along the bottom:
12. BOOK A LUNCH & LEARN AT YOUR OFFICE
Visit http://offer.witnessbench-example.com Call 555-014-2937
Designer: This call to action (CTA) for #12 needs to pop off of the page. It needs to draw the reader's eye. It needs depth, like the way a CTA button looks like on a website. Play around w/ idea to accomplish this (e.g., adding badges, icons, shapes, a picture, an image of someone presenting it, etc).
13. List my areas of specialization somewhere
• CPS & Matrimonial Issues
• Competency
• Juvenile Delinquency
• Criminal Sentencing
• Personal Injury and Civil Rights
• Immigration
• Fitness for Duty, SSD and Workers Comp
• Sex-Offenders
• IME and Neuropsychological Testing
• Behind-The-Scenes Consulting on A Contingency Fee
• Low-Price Initial Screening Evaluations
• Therapy Services & Programs for Litigants
14. Put this test somewhere and keep it subtle: I recognize the importance of your work. You can trust my assistance.
15. Put this in fine print somewhere (can be 2 lines): Fenwick and Torrance, LLC. 2018 New York Licensed Psychologist Lic. # 047213 - New Jersey Licensed Psychologist Lic. # 72K900315847

Target Market(s)

Lawyers

Industry/Entity Type

Hire

Font styles to use
Serif

Colors
ec1f27
ffffff

Requirements
Must have
• An awesome call to action. If the CTA doesn't catch the eye, then it won't work. The point of this postcard is to get them to that website so I can capture their email address. Anything else is a secondary gain. Consider 3-d design elements to give it pop and depth.
Should not have
• There's a big difference between a red rectangle and a red button on a website that has that 3d quality. This postcard has a lot of words. It can easily become just a bunch of text on a colorful piece of paper w/ a pic. Avoid this by segmenting the space, layering Diff color text on Diff color background and incorporating 3d design elements and shapes.

```html
<!DOCTYPE html>
<html lang="en">
<head>
<meta charset="utf-8">
<title>Fenwick and Torrance Postcard</title>
<link href="https://fonts.googleapis.com/css2?family=Lato:wght@400;700;900&display=swap" rel="stylesheet">
<style>
  :root {
    --red: #ec1f27;
    --deep-red: #9c0a10;
    --black: #111111;
    --white: #ffffff;
    --ink: #1a1a1a;
    --stage: #e9e6e2;
    --rule: #cfcfcf;
  }
  * { margin: 0; padding: 0; box-sizing: border-box; }
  html, body { width: 960px; height: 1200px; overflow: hidden; }
  body { background: var(--stage); font-family: 'Lato', sans-serif; color: var(--ink); position: relative; }

  .card { position: absolute; left: 47px; width: 867px; height: 472px; background: var(--white); overflow: hidden; box-shadow: 0 14px 24px rgba(0,0,0,.25); }
  .card--front { top: 74px; }
  .card--back { top: 646px; }

  .shapes { position: absolute; inset: 0; }

  .header { position: absolute; left: 33px; top: 20px; color: var(--red); font-weight: 700; font-size: 17.5px; line-height: 23.5px; }
  .header__headline { color: #2a2a2a; font-weight: 900; font-size: 22px; margin-top: 7px; }

  .sign { position: absolute; left: 23px; width: 380px; }
  .sign__label { position: relative; display: inline-block; white-space: nowrap; background: var(--red); color: var(--white); font-size: 10.5px; line-height: 14px; padding: 0 8px 0 10px; }
  .sign__label--long { font-size: 9.4px; padding-right: 6px; }
  .sign__label::after { content: ""; position: absolute; top: 0; right: -28px; width: 24px; height: 14px; background: var(--black); transform: skewX(40deg); }
  .sign__text { font-size: 9.2px; line-height: 12px; padding-left: 10px; margin-top: 5px; }

  .reassure { position: absolute; left: 506px; top: 20px; color: var(--red); font-weight: 700; font-size: 12.5px; line-height: 14.5px; width: 285px; }
  .specialties { position: absolute; left: 510px; top: 54px; list-style: none; font-size: 12px; line-height: 14.4px; }
  .specialties li { position: relative; padding-left: 20px; }
  .specialties li::before { content: "\2713"; position: absolute; left: 0; color: var(--red); font-size: 11px; }

  .gavel-art { position: absolute; left: 522px; top: 236px; width: 276px; height: 120px; border-radius: 50% 50% 10px 10px / 35% 35% 10px 10px; background: radial-gradient(ellipse at 45% 62%, #7a3e1c 0%, #9a5a30 40%, #d8b89c 68%, rgba(255,255,255,0) 80%); }

  .cta-left { position: absolute; left: 25px; top: 380px; color: var(--white); }
  .cta-left__intro { font-size: 14.5px; }
  .cta-left__url { font-size: 16px; font-weight: 700; margin: 6px 0 5px; display: flex; align-items: center; gap: 7px; }
  .cta-left__thanks { font-size: 14px; }

  .cta-right { position: absolute; left: 451px; top: 370px; color: var(--white); }
  .cta-right__phone { display: flex; align-items: center; gap: 22px; font-weight: 900; font-size: 46px; line-height: 50px; padding-left: 12px; }
  .cta-right__fine { font-size: 9.5px; line-height: 12px; margin-top: 10px; }

  .stamp-box { position: absolute; left: 714px; top: 38px; width: 91px; height: 105px; border: 1px solid var(--rule); }
  .address-line { position: absolute; left: 464px; width: 341px; height: 1px; background: var(--rule); }
</style>
</head>
<body>

<section class="card card--front">
  <svg class="shapes" viewBox="0 0 867 472" aria-hidden="true">
    <path d="M385 0 C455 15 493 70 488 150 C484 230 462 300 442 360 L421 360 C443 300 468 230 473 150 C478 80 450 25 385 0 Z" fill="var(--deep-red)"/>
    <path d="M0 360 L421 360 Q395 420 365 472 L0 472 Z" fill="var(--red)"/>
    <path d="M421 360 L442 360 Q420 420 397 472 L365 472 Q395 420 421 360 Z" fill="var(--deep-red)"/>
    <path d="M442 360 L867 360 L867 472 L397 472 Q420 420 442 360 Z" fill="var(--black)"/>
  </svg>

  <header class="header">
    <p>Dr. K.R. Torrance, Psy.D., NCEB</p>
    <p>Psychological Evaluator, Board-Certified Forensic</p>
    <p>Psychologist &amp; National Expert Witness</p>
    <h1 class="header__headline">4 Logical Signs of Proficiency &amp; Credibility</h1>
  </header>

  <div class="sign" style="top:135px">
    <span class="sign__label sign__label--long">Board Certified by the Continental Council of Courtroom Behavioral Science (CCCB)?</span>
    <p class="sign__text">Yes, I'm Board Certified. This mark of proficiency in forensic psychology is recognized by judicial decisions, statutes and regulations.</p>
  </div>
  <div class="sign" style="top:187px">
    <span class="sign__label">Fellow of the Cont. Fellowship of Legal Behavioral Study?</span>
    <p class="sign__text">Yes, I'm a CFLB Fellow, along with some of the field's most prominent leaders, comprising the academic arm of the CCCB.</p>
  </div>
  <div class="sign" style="top:240px">
    <span class="sign__label">A Recognized Leader Amongst Other Experts?</span>
    <p class="sign__text">I'm the 2018 duly elected President of the Hudson Valley Behavioral Guild Section on Courtroom Assessment, and a Board Member of the Coalition of Practitioners for Youth Safeguarding.</p>
  </div>
  <div class="sign" style="top:301px">
    <span class="sign__label">Positioned in Roles of Trust and Neutrality by Judges?</span>
    <p class="sign__text">Yes, I'm an in-house Harborview Juvenile Tribunal mental-health expert for proceedings regarding competency, imminent risk, sentencing, custody, child maltreatment and TPR.</p>
  </div>

  <p class="reassure">I recognize the importance of your work. You can trust my assistance.</p>
  <ul class="specialties">
    <li>CPS &amp; Matrimonial Issues</li>
    <li>Competency</li>
    <li>Juvenile Delinquency</li>
    <li>Criminal Sentencing</li>
    <li>Personal Injury and Civil Rights</li>
    <li>Immigration</li>
    <li>Fitness for Duty, SSD and Workers</li>
    <li>CompSex-Offenders</li>
    <li>IME and Neuropsychological Testing</li>
    <li>Behind-The-Scenes Consulting on A Contingency Fee</li>
    <li>Low-Price Initial Screening Evaluations</li>
    <li>Therapy Services &amp; Programs for Litigants</li>
  </ul>

  <div class="gavel-art" role="img" aria-label="Wooden judge's gavel with brass band resting on its sound block"></div>

  <div class="cta-left">
    <p class="cta-left__intro">To keep in touch, enter your email below.</p>
    <p class="cta-left__url">
      <svg width="17" height="17" viewBox="0 0 20 20" aria-hidden="true" fill="none" stroke="#fff" stroke-width="1.4">
        <circle cx="10" cy="10" r="8.5"/><ellipse cx="10" cy="10" rx="3.8" ry="8.5"/><path d="M1.5 10h17M3 5.5h14M3 14.5h14"/>
      </svg>
      http://offer.witnessbench-example.com
    </p>
    <p class="cta-left__thanks">I'll follow up with something to say, "Thank You."</p>
  </div>

  <div class="cta-right">
    <p class="cta-right__phone">
      <svg width="38" height="38" viewBox="0 0 40 40" aria-hidden="true" fill="none" stroke="#fff" stroke-width="2.4">
        <circle cx="20" cy="20" r="17"/>
        <path d="M14 11c-2 1-3 3-2 6 2 6 6 10 12 12 3 1 5 0 6-2l-4-4-3 2c-3-1-5-4-6-6l2-3z" fill="#fff" stroke="none"/>
        <path d="M22 11a8 8 0 0 1 7 7M22 15a4 4 0 0 1 3 3" stroke-width="1.8"/>
      </svg>
      555-014-2937
    </p>
    <p class="cta-right__fine">Fenwick and Torrance, LLC. 2018 New York Licensed Psychologist Lic. # 047213 -<br>New Jersey Licensed Psychologist Lic. # 72K900315847</p>
  </div>
</section>

<section class="card card--back" aria-label="Postcard back">
  <div class="stamp-box"></div>
  <div class="address-line" style="top:193px"></div>
  <div class="address-line" style="top:234px"></div>
  <div class="address-line" style="top:275px"></div>
</section>

</body>
</html>
```